The Harvest Compass

Cutting Through the Noise to What Actually Works.

Nutrition book

Target Market(s)

People looking to be or get healthy and eat right.

```html
<!DOCTYPE html>
<html lang="en">
<head>
<meta charset="utf-8">
<title>The Harvest Compass — Book Cover</title>
<link href="https://fonts.googleapis.com/css2?family=Archivo:wght@400;800&family=Roboto+Condensed:wght@700&display=swap" rel="stylesheet">
<style>
  :root {
    --backdrop: #e5e2dc;
    --cover: #201e1a;
    --cream: #f3eedc;
    --cream-top: #e9e2cf;
    --cream-shade: #bfb6a4;
    --sage: #7e9a86;
    --ink: #1d1b18;
  }
  html, body {
    margin: 0;
    width: 1200px;
    height: 1200px;
    overflow: hidden;
    background: var(--backdrop);
  }
  .cover {
    position: absolute;
    left: 254px;
    top: 84px;
    width: 692px;
    height: 1031px;
    background: var(--cover);
    color: var(--cream);
    font-family: "Archivo", sans-serif;
  }
  .cover__title {
    position: absolute;
    top: 52px;
    left: 0;
    right: 0;
    margin: 0;
    text-align: center;
    font-weight: 800;
    font-size: 68px;
    line-height: 68px;
    letter-spacing: 0.5px;
    text-transform: uppercase;
  }
  .cover__subtitle {
    position: absolute;
    top: 222px;
    left: 0;
    right: 0;
    margin: 0;
    text-align: center;
    font-weight: 400;
    font-size: 22px;
  }
  .hierarchy {
    position: absolute;
    left: 0;
    top: 0;
    width: 692px;
    height: 1031px;
  }
  .hierarchy__label {
    font-family: "Roboto Condensed", sans-serif;
    font-weight: 700;
    font-size: 46px;
    fill: var(--ink);
    text-anchor: middle;
  }
  .block-front { fill: var(--cream); }
  .block-top { fill: var(--cream-top); }
  .block-step { fill: var(--cream-shade); }
  .block-edge { fill: var(--sage); }
  .cover__author {
    position: absolute;
    top: 990px;
    left: 0;
    right: 0;
    margin: 0;
    text-align: center;
    font-weight: 800;
    font-size: 24px;
    letter-spacing: 8px;
  }
</style>
</head>
<body>
  <section class="cover">
    <h1 class="cover__title">The Harvest<br>Compass</h1>
    <p class="cover__subtitle">Cutting Through the Noise to What Actually Works.</p>

    <svg class="hierarchy" viewBox="0 0 692 1031" aria-label="Stacked hierarchy of nutrition priorities">
      <!-- Calories -->
      <polygon class="block-top" points="147,303 530,303 580,357 113,357"/>
      <rect class="block-front" x="113" y="357" width="467" height="88"/>
      <rect class="block-edge" x="113" y="445" width="467" height="9"/>
      <text class="hierarchy__label" x="346" y="418">CALORIES</text>

      <!-- Protein -->
      <rect class="block-front" x="144" y="454" width="404" height="93"/>
      <text class="hierarchy__label" x="346" y="516">PROTEIN</text>

      <!-- Food quality -->
      <polygon class="block-step" points="175,548 518,548 526,558 167,558"/>
      <rect class="block-front" x="167" y="558" width="359" height="92"/>
      <text class="hierarchy__label" x="346" y="620">FOOD QUALITY</text>

      <!-- Meal timing -->
      <polygon class="block-step" points="185,651 507,651 515,661 177,661"/>
      <rect class="block-front" x="177" y="661" width="338" height="93"/>
      <text class="hierarchy__label" x="346" y="723">MEAL TIMING</text>

      <!-- Supplements -->
      <polygon class="block-step" points="193,755 499,755 507,765 185,765"/>
      <rect class="block-front" x="185" y="765" width="322" height="93"/>
      <text class="hierarchy__label" x="346" y="827">SUPPLEMENTS</text>

      <!-- Noise -->
      <polygon class="block-step" points="210,859 477,859 485,868 202,868"/>
      <rect class="block-front" x="202" y="868" width="283" height="93"/>
      <text class="hierarchy__label" x="346" y="930">NOISE</text>
    </svg>

    <p class="cover__author">AUTHOR NAME</p>
  </section>
</body>
</html>
```